Graphic Design for Fit Process

I'm looking for something more like a graphic. The "paragraph descriptions" aren't necessarily important. The only thing that is important is this.

P - Pronation
A - Arches
W - Width
S - Size

If we could have a graphic that looks like a foot or a cute paw that is divided up to show the process, that would be much better.

Target Market(s)

Customer facing

Font styles to use
Serif

Requirements
Must have
• Graphics that are appealing and easy to understand

```html
<!DOCTYPE html>
<html lang="en">
<head>
<meta charset="utf-8">
<title>Fit Process Infographic</title>
<link href="https://fonts.googleapis.com/css2?family=Anton&display=swap" rel="stylesheet">
<style>
  :root {
    --page: #ffffff;
    --panel-edge: #c8c9cb;
    --panel-center: #eeeff0;
    --heart: #ee4b25;
    --heart-shadow: #b9babc;
    --fit-shadow: #b5341b;
    --white: #ffffff;
    --check-word: #f26a3a;
    --ink: #2b1519;
    --blue: #2e86c8;
    --blue-soft: #34a3dc;
    --orange: #f4872a;
    --orange-soft: #f9ad2c;
    --red: #ee4b25;
    --red-soft: #f06a37;
    --yellow: #f9d30c;
    --yellow-soft: #f8e620;
    --caption: #bcbdbf;
    --brand: #2e86c8;
  }
  html, body {
    margin: 0;
    padding: 0;
    width: 1189px;
    height: 1200px;
    overflow: hidden;
    background: var(--page);
  }
  .canvas {
    display: block;
    width: 1189px;
    height: 1200px;
  }
  .display {
    font-family: "Anton", sans-serif;
  }
  .fit-word { fill: var(--white); font-size: 222px; }
  .fit-shadow { fill: var(--fit-shadow); font-size: 222px; }
  .process-word { fill: var(--white); font-size: 44px; letter-spacing: 9px; }
  .check-word { fill: var(--check-word); font-size: 28px; }
  .step-label { fill: var(--ink); font-size: 46px; }
  .brand-name { fill: var(--brand); font-size: 30px; letter-spacing: 0.5px; }
  .caption { fill: var(--caption); font-size: 38px; }
  .tick { fill: none; stroke-width: 7; stroke-linecap: round; stroke-linejoin: round; }
</style>
</head>
<body>
<svg class="canvas" viewBox="0 0 1140 1160" preserveAspectRatio="none" xmlns="http://www.w3.org/2000/svg">
  <defs>
    <radialGradient id="panelGlow" cx="50%" cy="48%" r="65%">
      <stop offset="0%" stop-color="var(--panel-center)"/>
      <stop offset="100%" stop-color="var(--panel-edge)"/>
    </radialGradient>
  </defs>

  <!-- panel -->
  <rect class="panel" x="171" y="172" width="800" height="808" fill="url(#panelGlow)"/>

  <!-- paw toes -->
  <g class="toe toe-pronation">
    <ellipse cx="328" cy="562" rx="70" ry="84" transform="rotate(28 328 562)" fill="var(--blue)"/>
    <circle cx="330" cy="552" r="34" fill="var(--blue-soft)"/>
    <path class="tick" d="M313 551 L326 563 L347 540" stroke="var(--blue)"/>
  </g>
  <g class="toe toe-arches">
    <ellipse cx="463" cy="712" rx="74" ry="98" transform="rotate(18 463 712)" fill="var(--orange)"/>
    <circle cx="465" cy="710" r="32" fill="var(--orange-soft)"/>
    <path class="tick" d="M450 710 L462 721 L482 699" stroke="var(--orange)"/>
  </g>
  <g class="toe toe-width">
    <ellipse cx="669" cy="720" rx="72" ry="98" transform="rotate(-8 669 720)" fill="var(--red)"/>
    <circle cx="676" cy="724" r="32" fill="var(--red-soft)"/>
    <path class="tick" d="M661 724 L673 735 L693 713" stroke="var(--red)"/>
  </g>
  <g class="toe toe-size">
    <ellipse cx="812" cy="580" rx="70" ry="80" transform="rotate(-30 812 580)" fill="var(--yellow)"/>
    <circle cx="816" cy="590" r="34" fill="var(--yellow-soft)"/>
    <path class="tick" d="M800 590 L813 602 L834 579" stroke="var(--yellow)"/>
  </g>

  <!-- heart pad -->
  <path class="heart-shadow" transform="translate(8 8)" fill="var(--heart-shadow)"
    d="M578 283 C545 238 500 220 452 222 C382 225 332 284 332 352 C332 412 362 452 402 492 L558 646 Q575 662 592 646 L760 480 C800 440 822 402 822 350 C822 280 770 224 702 222 C652 220 612 244 578 283 Z"/>
  <path class="heart" fill="var(--heart)"
    d="M578 283 C545 238 500 220 452 222 C382 225 332 284 332 352 C332 412 362 452 402 492 L558 646 Q575 662 592 646 L760 480 C800 440 822 402 822 350 C822 280 770 224 702 222 C652 220 612 244 578 283 Z"/>

  <text class="display fit-shadow" x="592" y="486" text-anchor="middle">FIT</text>
  <text class="display fit-word" x="586" y="482" text-anchor="middle">FIT</text>
  <text class="display process-word" x="578" y="527" text-anchor="middle">PROCESS</text>
  <text class="display check-word" x="578" y="575" text-anchor="middle">CHECK...</text>

  <!-- step labels -->
  <text class="display step-label" x="373" y="602" text-anchor="middle">PRONATION</text>
  <text class="display step-label" x="388" y="730" text-anchor="middle">ARCHES</text>
  <text class="display step-label" x="611" y="748" text-anchor="middle">WIDTH</text>
  <text class="display step-label" x="762" y="634" text-anchor="middle">SIZE</text>

  <!-- brand -->
  <rect class="brand-mark" x="404" y="872" width="40" height="40" fill="var(--brand)"/>
  <text class="display brand-name" x="458" y="906">CANYON STRIDE RUNNING CO.</text>

  <!-- caption -->
  <text class="display caption" x="570" y="1048" text-anchor="middle">INFOGRAPHIC</text>
</svg>
</body>
</html>
```